Do i have coronavirus, flue or cold?

Using information from QRV and government agencies we want to make a easy to read infographic helping patients see if they have coronavirus, the flu or a cold. Using a flow diagram or whatever you think will make it easy to read and digest for the average lamen.

Information is in the word document and in the chart.

We are www.tovipharm.co.uk attached is our brand guidelines, we will be putting this infographic on our website and email/sms it to all of our 300,000 patients.

```html
<!DOCTYPE html>
<html lang="en">
<head>
<meta charset="utf-8">
<title>Do I have coronavirus, the flu, or a cold?</title>
<link rel="stylesheet" href="https://fonts.googleapis.com/css2?family=Figtree:wght@400;500;600;700&family=Poppins:ital,wght@1,700&display=swap">
<style>
  :root {
    --page: #f4f6f6;
    --panel: #ecf3f5;
    --ink: #0b0b3b;
    --label-ink: #2a2a2a;
    --corona: #3333bb;
    --corona-soft: #d0d9f8;
    --flu: #ffa27c;
    --flu-soft: #f5d0c3;
    --cold: #000033;
    --cold-soft: #d7dfe0;
    --dark: #474747;
    --hot: #f75f1f;
    --amber: #ffd872;
    --lime: #c0ee66;
    --mint: #b0ffcb;
    --white: #ffffff;
  }
  * { box-sizing: border-box; margin: 0; padding: 0; }
  html, body { width: 1200px; height: 1200px; overflow: hidden; background: var(--page); }
  body { font-family: "Figtree", sans-serif; position: relative; }
  .panel { position: absolute; left: 188px; top: 0; width: 824px; height: 1200px; background: var(--panel); }
  .title {
    position: absolute; left: 0; width: 1200px; top: 56px; text-align: center;
    font-family: "Poppins", sans-serif; font-style: italic; font-weight: 700;
    font-size: 31px; color: var(--ink); letter-spacing: 0.2px;
  }
  .row-band {
    position: absolute; left: 253px; width: 521px; height: 73px;
    top: calc(253px + var(--r) * 89px); background: var(--white);
    border-radius: 37px 0 0 37px; box-shadow: 0 2px 4px rgba(0,0,0,0.04);
  }
  .row-label {
    position: absolute; left: 253px; width: 146px; height: 73px;
    top: calc(253px + var(--r) * 89px);
    display: flex; align-items: center; justify-content: center;
    font-size: 13px; font-weight: 500; line-height: 1.15; color: var(--label-ink);
    text-align: center; z-index: 2;
  }
  .row-label.left { justify-content: flex-start; padding-left: 42px; text-align: left; }
  .column { position: absolute; top: 169px; width: 173px; height: 868px; z-index: 1; }
  .column-head {
    height: 58px; border-radius: 0 37px 0 0; color: var(--white);
    font-weight: 700; font-size: 15px; display: flex; align-items: center; padding-left: 12px;
  }
  .column-body { height: 810px; }
  .col-corona { left: 399px; } .col-corona .column-head { background: var(--corona); } .col-corona .column-body { background: var(--corona-soft); }
  .col-flu { left: 586px; } .col-flu .column-head { background: var(--flu); } .col-flu .column-body { background: var(--flu-soft); }
  .col-cold { left: 774px; } .col-cold .column-head { background: var(--cold); padding-left: 18px; } .col-cold .column-body { background: var(--cold-soft); }
  .track {
    position: absolute; left: 0; width: 154px; height: 55px;
    top: calc(94px + var(--r) * 89px);
    border: 1px solid rgba(255,255,255,0.7); border-left: none; border-radius: 0 28px 28px 0;
  }
  .pill {
    position: absolute; left: 0; height: 53px; top: calc(95px + var(--r) * 89px);
    border-radius: 0 27px 27px 0; display: flex; align-items: center; padding-left: 12px;
    font-size: 13px; font-weight: 600; white-space: nowrap; z-index: 2;
  }
  .pill svg { position: absolute; right: 26px; top: 16px; }
  .is-dark { background: var(--dark); color: var(--white); }
  .is-hot { background: var(--hot); color: var(--white); }
  .is-amber { background: var(--amber); color: #333; font-weight: 500; }
  .is-lime { background: var(--lime); color: #333; font-weight: 500; }
  .is-mint { background: var(--mint); color: #333; font-weight: 500; }
  .source { position: absolute; left: 218px; top: 1126px; font-size: 21px; color: var(--ink); }
  .brand {
    position: absolute; left: 545px; top: 1110px; width: 112px;
    display: flex; align-items: center; gap: 6px;
    font-size: 17px; font-weight: 700; color: var(--corona);
  }
  .brand-dot { width: 12px; height: 12px; border-radius: 50%; background: var(--corona); }
</style>
</head>
<body>
  <div class="panel"></div>
  <h1 class="title">Do I have coronavirus, the flu, or a cold?</h1>

  <div class="row-band" style="--r:0"></div><div class="row-band" style="--r:1"></div>
  <div class="row-band" style="--r:2"></div><div class="row-band" style="--r:3"></div>
  <div class="row-band" style="--r:4"></div><div class="row-band" style="--r:5"></div>
  <div class="row-band" style="--r:6"></div><div class="row-band" style="--r:7"></div>
  <div class="row-band" style="--r:8"></div>

  <div class="row-label" style="--r:0;padding-left:30px">Fever</div>
  <div class="row-label" style="--r:1;padding-left:30px">Cough</div>
  <div class="row-label" style="--r:2;padding-left:12px">Tiredness</div>
  <div class="row-label" style="--r:3;padding-left:12px">Shortness<br>of breath</div>
  <div class="row-label" style="--r:4;padding-left:30px">Muscle<br>aches</div>
  <div class="row-label left" style="--r:5">Headache</div>
  <div class="row-label left" style="--r:6">Sore<br>Throat</div>
  <div class="row-label left" style="--r:7">Stuffy or<br>runny<br>nose</div>
  <div class="row-label left" style="--r:8">Sneezing</div>

  <section class="column col-corona">
    <div class="column-head">CORONAVIRUS</div>
    <div class="column-body"></div>
    <div class="pill is-dark" style="--r:0;width:130px">Yes</div>
    <div class="pill is-hot" style="--r:1;width:151px">Yes (Dry)</div>
    <div class="pill is-dark" style="--r:2;width:130px">Yes</div>
    <div class="pill is-dark" style="--r:3;width:130px">Yes</div>
    <div class="pill is-dark" style="--r:4;width:130px">Yes</div>
    <div class="pill is-amber" style="--r:5;width:89px">Sometimes</div>
    <div class="pill is-amber" style="--r:6;width:89px">Sometimes</div>
    <div class="pill is-lime" style="--r:7;width:66px">Rare</div>
    <div class="pill is-mint" style="--r:8;width:56px">No</div>
  </section>

  <section class="column col-flu">
    <div class="column-head">FLU</div>
    <div class="column-body"></div>
    <div class="pill is-hot" style="--r:0;width:153px">Yes (High)
      <svg width="16" height="22" viewBox="0 0 16 22"><path d="M8 21V2M1 9l7-7 7 7" fill="none" stroke="#fff" stroke-width="2"/></svg></div>
    <div class="pill is-dark" style="--r:1;width:129px">Yes</div>
    <div class="pill is-dark" style="--r:2;width:129px">Yes</div>
    <div class="pill is-dark" style="--r:3;width:129px">Yes</div>
    <div class="pill is-hot" style="--r:4;width:153px">Yes (Often)
      <svg width="16" height="22" viewBox="0 0 16 22"><path d="M8 21V2M1 9l7-7 7 7" fill="none" stroke="#fff" stroke-width="2"/></svg></div>
    <div class="pill is-dark" style="--r:5;width:129px;padding-left:19px">Yes</div>
    <div class="pill is-amber" style="--r:6;width:88px">Sometimes</div>
    <div class="pill is-amber" style="--r:7;width:88px">Sometimes</div>
    <div class="pill is-amber" style="--r:8;width:88px">Sometimes</div>
  </section>

  <section class="column col-cold">
    <div class="column-head">COLD</div>
    <div class="column-body"></div>
    <div class="track" style="--r:0"></div><div class="track" style="--r:1"></div>
    <div class="track" style="--r:2"></div><div class="track" style="--r:3"></div>
    <div class="track" style="--r:4"></div><div class="track" style="--r:5"></div>
    <div class="track" style="--r:6"></div><div class="track" style="--r:7"></div>
    <div class="track" style="--r:8"></div>
    <div class="pill is-lime" style="--r:0;width:66px;padding-left:18px">Rare</div>
    <div class="pill is-amber" style="--r:1;width:91px;padding-left:18px">Moderate</div>
    <div class="pill is-mint" style="--r:2;width:56px;padding-left:18px">Mild</div>
    <div class="pill is-lime" style="--r:3;width:66px;padding-left:18px">Rare</div>
    <div class="pill is-lime" style="--r:4;width:66px;padding-left:18px">Rare</div>
    <div class="pill is-lime" style="--r:5;width:66px;padding-left:18px">Rare</div>
    <div class="pill is-dark" style="--r:6;width:120px;padding-left:18px">Yes</div>
    <div class="pill is-dark" style="--r:7;width:120px;padding-left:18px">Yes</div>
    <div class="pill is-dark" style="--r:8;width:120px;padding-left:18px">Yes</div>
  </section>

  <p class="source">source: QRV, NHA</p>
  <div class="brand"><span class="brand-dot"></span>tovipharm</div>
</body>
</html>
```